Vacation Rental business needs a prospective client flyer

We are a short-term vacation rental company in Steamboat Springs, Colorado called "Tidy Maple Cabins". We are looking to find new clients in the area by handing out flyers to the local Realtors to recommend using us to their clients.

We would like to touch on our low management fee of 18% and are local hands on approach.

Logo sheet is included for color and logo use.

```html
<!DOCTYPE html>
<html lang="en">
<head>
<meta charset="utf-8">
<title>Tidy Maple Cabins – Flyer</title>
<link href="https://fonts.googleapis.com/css2?family=Caveat:wght@500&family=Montserrat:wght@300;400;500&display=swap" rel="stylesheet">
<style>
  :root {
    --brand-blue: #1d6f9a;
    --deep-blue: #0f6aa0;
    --light-blue: #3aa3c6;
    --snow: #f1f4f7;
    --snow-shade: #e2e8ee;
    --ink: #2a2f35;
    --muted: #6f7378;
    --white: #ffffff;
  }
  * { margin: 0; padding: 0; box-sizing: border-box; }
  html, body { width: 960px; height: 1200px; overflow: hidden; background: var(--snow); }
  .flyer {
    position: relative; width: 960px; height: 1200px; overflow: hidden;
    background: linear-gradient(180deg, #fbfcfd 0%, var(--snow) 100%);
    font-family: "Montserrat", sans-serif; color: var(--ink);
  }
  .layer { position: absolute; left: 0; top: 0; width: 960px; height: 1200px; }
  .brand {
    position: absolute; top: 78px; left: 0; width: 960px; text-align: center;
  }
  .brand-name {
    font-family: "Montserrat", sans-serif; font-weight: 500; font-size: 54px;
    color: var(--brand-blue); letter-spacing: 1px;
  }
  .brand-place {
    margin-top: 14px; font-weight: 300; font-size: 24px; letter-spacing: 12px;
    color: #55595e;
  }
  .headline {
    position: absolute; top: 722px; left: 0; width: 960px; text-align: center;
    font-family: "Caveat", cursive; font-weight: 500; font-size: 104px;
    color: var(--brand-blue); line-height: 1;
  }
  .intro {
    position: absolute; top: 840px; left: 150px; width: 660px; text-align: center;
    font-weight: 400; font-size: 23px; line-height: 34px; color: var(--ink);
  }
  .details {
    position: absolute; top: 952px; left: 120px; width: 720px; text-align: center;
    font-weight: 400; font-size: 16.5px; line-height: 25px; color: #33383d;
  }
  .fee-pill {
    position: absolute; top: 1078px; left: 126px; width: 708px; height: 35px;
    background: var(--white); border-radius: 18px; text-align: center;
    font-weight: 500; font-size: 16.5px; line-height: 35px; color: #1c1f22;
  }
  .contact {
    position: absolute; top: 1135px; left: 0; width: 960px;
    display: flex; justify-content: center; align-items: center;
    color: var(--white); font-weight: 500; font-size: 18px;
  }
  .contact-item { display: flex; align-items: center; gap: 8px; padding: 0 28px; }
  .contact-item svg { width: 17px; height: 17px; }
  .divider { width: 1.5px; height: 24px; background: var(--white); }
</style>
</head>
<body>
<main class="flyer">

  <svg class="layer hero-photo" role="img" aria-label="Photo of a family having a snowball fight in front of a log cabin in the snow" viewBox="0 0 960 1200">
    <defs>
      <linearGradient id="heroTones" x1="0" y1="0" x2="1" y2="0">
        <stop offset="0" stop-color="#b8403a"/>
        <stop offset="0.28" stop-color="#d6d9dd"/>
        <stop offset="0.48" stop-color="#3aa1cf"/>
        <stop offset="0.66" stop-color="#e6c7d3"/>
        <stop offset="0.82" stop-color="#b98a68"/>
        <stop offset="1" stop-color="#7a5038"/>
      </linearGradient>
      <linearGradient id="heroFade" x1="0" y1="0" x2="0" y2="1">
        <stop offset="0" stop-color="#fbfcfd" stop-opacity="1"/>
        <stop offset="0.3" stop-color="#fbfcfd" stop-opacity="0.55"/>
        <stop offset="0.6" stop-color="#fbfcfd" stop-opacity="0.15"/>
        <stop offset="1" stop-color="#f3f5f8" stop-opacity="0.55"/>
      </linearGradient>
    </defs>
    <rect x="0" y="110" width="960" height="620" fill="url(#heroTones)"/>
    <rect x="0" y="110" width="960" height="620" fill="url(#heroFade)"/>
  </svg>

  <svg class="layer snow-bands" aria-hidden="true" viewBox="0 0 960 1200">
    <defs>
      <linearGradient id="snowFill" x1="0" y1="0" x2="0" y2="1">
        <stop offset="0" stop-color="#e9eef3"/>
        <stop offset="1" stop-color="#f4f6f8"/>
      </linearGradient>
      <linearGradient id="bandFill" x1="0" y1="0" x2="0" y2="1">
        <stop offset="0" stop-color="var(--deep-blue)"/>
        <stop offset="1" stop-color="var(--light-blue)"/>
      </linearGradient>
    </defs>
    <path d="M0 616 C 180 596, 360 630, 500 668 C 640 706, 800 705, 960 640 L960 1200 L0 1200 Z" fill="url(#snowFill)"/>
    <path d="M0 616 C 180 596, 360 630, 500 668 C 640 706, 800 705, 960 640" fill="none" stroke="var(--brand-blue)" stroke-width="2"/>
    <path d="M0 1085 C 150 1025, 300 1008, 420 1024 C 560 1044, 630 1080, 770 1050 C 860 1030, 920 1000, 960 968 L960 1200 L0 1200 Z" fill="url(#bandFill)"/>
    <g class="intro-frame" fill="none" stroke="var(--brand-blue)" stroke-width="1.5">
      <path d="M238 793 H107 Q103 793 103 797 V921 Q103 925 107 925 H348"/>
      <path d="M723 793 H853 Q857 793 857 797 V921 Q857 925 853 925 H610"/>
    </g>
  </svg>

  <header class="brand">
    <div class="brand-name">Tidy Maple Cabins</div>
    <div class="brand-place">steamboat springs, co</div>
  </header>

  <h1 class="headline">snowfall in love</h1>

  <p class="intro">Welcome to Tidy Maple Cabins! Our properties in Steamboat Springs have everything you need for a great vacation!</p>

  <p class="details">We offer a wide range of properties that all include WiFi, Full Kitchens, Hot Tubs and more. Book directly with us today!</p>

  <div class="fee-pill">Low management fee of 18% and are local hands on approach</div>

  <footer class="contact">
    <div class="contact-item">
      <svg viewBox="0 0 20 20" fill="none" stroke="#fff" stroke-width="1.5"><circle cx="10" cy="10" r="8"/><ellipse cx="10" cy="10" rx="3.5" ry="8"/><path d="M2 10h16M3.5 6h13M3.5 14h13"/></svg>
      <span>www.TidyMapleCabins.com</span>
    </div>
    <span class="divider"></span>
    <div class="contact-item">
      <svg viewBox="0 0 20 20" fill="none" stroke="#fff" stroke-width="1.5"><circle cx="10" cy="10" r="8.5"/><path d="M7 5.5l1.6 2.4-1 1.2c.6 1.3 1.6 2.3 2.9 2.9l1.2-1 2.4 1.6-.8 1.6c-3.6-.3-6.9-3.6-7.2-7.2z"/></svg>
      <span>(970) 555-0148</span>
    </div>
    <span class="divider"></span>
    <div class="contact-item">
      <svg viewBox="0 0 20 20" fill="none" stroke="#fff" stroke-width="1.5"><rect x="2.5" y="5" width="15" height="10" rx="1"/><path d="M2.5 5.5l7.5 5.5 7.5-5.5"/></svg>
      <span>info@tidymaplecabins.com</span>
    </div>
  </footer>

</main>
</body>
</html>
```